TLR Property - Business Cards

Looking for a business card & general letterhead, signage etc design for our new logo.

Colours:
000a20
0056a2
00b5ef
0088ce
68cef2

Fonts:
Poppins
Karla

Please keep look and feel of new brand - example in the zip package I sent.

```html
<!DOCTYPE html>
<html lang="en">
<head>
<meta charset="utf-8">
<title>TLR Property – Business Cards</title>
<link rel="stylesheet" href="https://fonts.googleapis.com/css2?family=Poppins:wght@300;400;600;700;800&display=swap">
<style>
  :root {
    --ink-navy: #000a20;
    --card-back: #101229;
    --brand-deep: #0056a2;
    --brand-mid: #0088ce;
    --brand-bright: #00b5ef;
    --brand-light: #68cef2;
    --text-dark: #1c2233;
    --paper: #ffffff;
    --stage: #e6e8ec;
  }
  * { margin: 0; padding: 0; box-sizing: border-box; }
  html, body { width: 1200px; height: 912px; overflow: hidden; }
  body {
    background: var(--stage);
    font-family: "Poppins", sans-serif;
    position: relative;
  }
  .card {
    position: absolute;
    width: 540px;
    height: 310px;
    border-radius: 4px;
    box-shadow: 0 10px 28px rgba(0, 10, 32, 0.18);
    overflow: hidden;
  }
  /* back of card */
  .card--back {
    left: 110px;
    top: 100px;
    background: var(--card-back);
  }
  .card--back .wordmark {
    position: absolute;
    left: 0; right: 0; top: 120px;
    display: flex; align-items: center; justify-content: center; gap: 14px;
    color: var(--paper);
    font-weight: 700;
    font-size: 44px;
    letter-spacing: 1px;
  }
  .dot {
    width: 22px; height: 22px; border-radius: 50%;
    background: var(--brand-bright);
    flex: none;
  }
  /* front of card */
  .card--front {
    left: 550px;
    top: 500px;
    background: var(--paper);
  }
  .card--front .wordmark {
    position: absolute;
    left: 0; right: 0; top: 34px;
    display: flex; align-items: center; justify-content: center; gap: 12px;
    color: var(--brand-deep);
    font-weight: 700;
    font-size: 38px;
  }
  .person {
    position: absolute;
    left: 0; right: 0; top: 112px;
    text-align: center;
  }
  .person__name {
    font-weight: 800;
    font-size: 24px;
    letter-spacing: 0.5px;
    color: var(--brand-deep);
  }
  .person__name .surname { color: var(--brand-mid); }
  .person__role {
    font-weight: 400;
    font-size: 13px;
    color: var(--text-dark);
    margin-top: -2px;
  }
  .rule {
    position: absolute;
    left: 36px; right: 36px; top: 184px;
    height: 1.5px;
    background: var(--brand-mid);
  }
  .contact {
    position: absolute;
    left: 36px; bottom: 30px;
    list-style: none;
    font-size: 13px;
    font-weight: 400;
    color: var(--text-dark);
    line-height: 1.55;
  }
  .contact li { display: flex; align-items: center; gap: 7px; }
  .contact svg { width: 12px; height: 12px; flex: none; }
  .address {
    position: absolute;
    right: 36px; bottom: 30px;
    text-align: right;
    font-style: normal;
    font-size: 13px;
    font-weight: 400;
    color: var(--text-dark);
    line-height: 1.55;
  }
</style>
</head>
<body>
  <section class="card card--back" aria-label="Business card back">
    <div class="wordmark"><span class="dot"></span>TLR Property</div>
  </section>

  <section class="card card--front" aria-label="Business card front">
    <div class="wordmark"><span class="dot"></span>TLR Property</div>
    <div class="person">
      <div class="person__name">DANA <span class="surname">MERCER</span></div>
      <div class="person__role">Founder &amp; Principal</div>
    </div>
    <div class="rule"></div>
    <ul class="contact">
      <li>
        <svg viewBox="0 0 24 24" fill="var(--brand-deep)"><path d="M6.6 10.8a15 15 0 0 0 6.6 6.6l2.2-2.2a1 1 0 0 1 1-.25 11.4 11.4 0 0 0 3.6.57 1 1 0 0 1 1 1V20a1 1 0 0 1-1 1A17 17 0 0 1 3 4a1 1 0 0 1 1-1h3.5a1 1 0 0 1 1 1c0 1.250.2 2.45.57 3.57a1 1 0 0 1-.25 1z"/></svg>
        +1- 415-555-0148
      </li>
      <li>
        <svg viewBox="0 0 24 24" fill="none" stroke="var(--brand-deep)" stroke-width="2.4"><rect x="3" y="5" width="18" height="14" rx="1.5"/><path d="M3 6l9 7 9-7"/></svg>
        info@tlrproperty.com
      </li>
      <li>
        <svg viewBox="0 0 24 24" fill="none" stroke="var(--brand-deep)" stroke-width="2.2"><circle cx="12" cy="12" r="9"/><path d="M3 12h18M12 3c3 3.5 3 14.5 0 18M12 3c-3 3.5-3 14.5 0 18"/></svg>
        www.tlrproperty.com
      </li>
    </ul>
    <address class="address">
      4120 North Ridge Avenue<br>
      #27, Suite Lakeview Park
    </address>
  </section>
</body>
</html>
```